Kelvora Ledger Web Design Contest

We would like for you to design a website for www.kelvoraledger-example.com. Kelvora Ledger is a CPA Firm offering accounting, auditing, and tax preparation services.

We would like to have a consistent feel with the logo, business card, envelope, and stationary designs that were created by another designer on PlanHive. Examples of each are attached. We would like the website to have a clean/modern style.

The website should include the following:

1. A general "Welcome" landing page
2. A "About the Company" page
3. A "Services Offered" page
4. A "Contact Us" form
5. A button for "Sign up for Newsletter"

Target Market(s)

Individuals and businesses that require accounting, auditing, and tax preparation services from a CPA.

Industry/Entity Type

Accounting

Coding

Number of Pages Required

5+ page

Font styles to use
Other font styles liked:
• Trebuchet or similar

Requirements
Must have
• Consistent feel with logo and letterhead. The gray and blue bar on the letterhead should be incorporated into the website design.

```html
<!DOCTYPE html>
<html lang="en">
<head>
<meta charset="utf-8">
<title>Kelvora Ledger — Accounting · Audit · Tax Services</title>
<link href="https://fonts.googleapis.com/css2?family=Raleway:wght@400;500;600&family=Carlito:wght@400;700&display=swap" rel="stylesheet">
<style>
  :root{
    --page:#333333;
    --white:#ffffff;
    --navy:#0a1f66;
    --brand:#1b2f6e;
    --purple:#7708e0;
    --orange:#ff9500;
    --charcoal:#3a3a3a;
    --green:#22c229;
    --gold:#deaf02;
    --rust:#e05a07;
    --violet:#7802e0;
    --sky:#06a0df;
    --leaf:#1bb503;
    --brown:#7b3208;
    --red:#d81b0b;
    --steel:#135886;
  }
  *{margin:0;padding:0;box-sizing:border-box}
  html,body{width:1044px;height:1200px;overflow:hidden;background:var(--page)}
  body{font-family:"Carlito",Calibri,sans-serif;color:var(--white)}
  .site{position:absolute;left:0;top:0;width:1270px;height:1460px;transform:scale(0.8221);transform-origin:0 0}
  .block{position:absolute}
  .heading{font-family:"Raleway",sans-serif}

  .masthead{left:50px;top:3px;width:1172px;height:98px;background:var(--white)}
  .brand{position:absolute;left:18px;top:12px;display:flex;align-items:center;gap:12px}
  .brand-mark{width:40px;height:40px;border:3px solid var(--brand)}
  .brand-name{font-family:"Carlito",sans-serif;font-size:22px;font-weight:700;color:var(--brand);letter-spacing:.5px;text-transform:uppercase}
  .brand-tag{position:absolute;left:32px;top:80px;font-size:10px;color:#333;letter-spacing:1px}
  .nav{position:absolute;right:0;top:0;height:98px;display:flex}
  .nav a{display:flex;align-items:center;justify-content:center;color:var(--white);text-decoration:none;font-size:14px;height:98px}
  .nav .home{width:76px;background:var(--navy)}
  .nav .about{width:177px;background:var(--purple);margin-left:1px}
  .nav .services{width:140px;background:var(--orange)}
  .nav .contact{width:118px;background:var(--charcoal)}

  .hero{left:50px;top:106px;width:1170px;height:569px;background:radial-gradient(ellipse at 20% 75%,#c8a48c 0%,#e8e3de 30%,#cfd6db 60%,#8a949c 100%)}
  .hero-panel{position:absolute;left:266px;top:198px;width:706px;height:302px;background:rgba(40,40,40,.95);text-align:center}
  .hero-panel h1{font-family:"Raleway",sans-serif;font-weight:500;font-size:48px;line-height:58px;margin-top:32px;letter-spacing:.5px}
  .hero-panel p{font-size:14px;line-height:17px;margin:18px 40px 0}
  .read-more{position:absolute;left:318px;top:236px;width:110px;height:36px;background:var(--navy);display:flex;align-items:center;justify-content:center;font-size:14px}
  .circle-btn{position:absolute;border:2px solid var(--white);border-radius:50%;display:flex;align-items:center;justify-content:center}

  .tile{text-align:center;display:flex;flex-direction:column;align-items:center}
  .tile-title{font-family:"Raleway",sans-serif;font-weight:600;font-size:24px}
  .icon-ring{width:94px;height:94px;border:1.5px solid var(--white);border-radius:50%;display:flex;align-items:center;justify-content:center}
  .small-ring{width:58px;height:58px;border:1.5px solid var(--white);border-radius:50%;display:flex;align-items:center;justify-content:center}

  .offering{left:50px;top:680px;width:388px;height:241px;background:var(--green)}
  .offering h2{font-family:"Raleway",sans-serif;font-weight:500;font-size:36px;margin-top:38px}
  .offering ul{list-style:none;font-family:"Raleway",sans-serif;font-size:24px;line-height:29px;margin-top:20px}
  .welcome{left:441px;top:680px;width:388px;height:241px;background:var(--gold)}
  .welcome h2{font-family:"Raleway",sans-serif;font-weight:500;font-size:22px;line-height:26px;margin-top:36px}
  .welcome p{font-size:13.5px;line-height:17px;text-align:justify;margin:10px 25px 0}
  .about{left:832px;top:680px;width:388px;height:241px;background:var(--rust)}
  .services{left:50px;top:925px;width:428px;height:236px;background:var(--violet)}
  .testimonials{left:481px;top:925px;width:318px;height:236px;background:var(--sky)}
  .newsletter{left:802px;top:925px;width:418px;height:236px;background:var(--leaf)}
  .follow{left:50px;top:1165px;width:596px;height:215px;background:var(--brown)}
  .contact{left:649px;top:1165px;width:571px;height:215px;background:var(--red)}
  .row-icons{display:flex;gap:32px;margin-top:30px}
  .footer{left:50px;top:1384px;width:1170px;height:76px;background:var(--steel);display:flex;align-items:center;justify-content:center;font-size:14px}
</style>
</head>
<body>
<div class="site">

  <header class="block masthead">
    <div class="brand">
      <div class="brand-mark"></div>
      <div class="brand-name">Kelvora Ledger</div>
    </div>
    <div class="brand-tag">Accounting · Audit · Tax Services</div>
    <nav class="nav">
      <a class="home">Home</a>
      <a class="about">About the Company</a>
      <a class="services">Services Offered</a>
      <a class="contact">Contact Us</a>
    </nav>
  </header>

  <section class="block hero" role="img" aria-label="Soft-focus photo of a hand on a computer mouse beside a keyboard on a desk">
    <div class="hero-panel">
      <h1>STRATEGIES THAT DRIVE<br>BUSINESS RESULTS</h1>
      <p>Lorem ipsum dolor sit amet, consectetur adipiscing elit, sed do eiusmod tempor incididunt ut labore et dolore magna aliqua. Ut enim ad minim veniam, quis nostrud exercitation ullamco laborisLorem ipsum dolor sit amet, consectetur adipiscing elit, sed do eiusmod tempor incididunt ut labore</p>
      <div class="read-more">READ MORE</div>
      <div class="circle-btn" style="left:13px;top:233px;width:42px;height:42px">
        <svg width="14" height="14" viewBox="0 0 14 14"><path d="M9 2 L4 7 L9 12" fill="none" stroke="#fff" stroke-width="2"/></svg>
      </div>
      <div class="circle-btn" style="left:642px;top:225px;width:42px;height:42px">
        <svg width="14" height="14" viewBox="0 0 14 14"><path d="M5 2 L10 7 L5 12" fill="none" stroke="#fff" stroke-width="2"/></svg>
      </div>
    </div>
  </section>

  <section class="block tile offering">
    <h2>OFFERING</h2>
    <ul><li>Accounting</li><li>Auditing</li><li>Tax Preparation</li></ul>
  </section>

  <section class="block tile welcome">
    <h2>WELCOME TO<br>KELVORA LEDGER</h2>
    <p>Lorem ipsum dolor sit amet, consectetur adipiscing elit, sed do eiusmod tempor incididunt ut labore et dolore magna aliqua. onsectetur adipiscing elit, sed do eiusmod ut labore et dolore magna aliqua.</p>
    <div class="circle-btn" style="left:320px;top:182px;width:38px;height:38px;border-width:1.5px">
      <svg width="12" height="14" viewBox="0 0 12 14"><path d="M4 2 L9 7 L4 12" fill="none" stroke="#fff" stroke-width="1.5"/></svg>
    </div>
  </section>

  <section class="block tile about">
    <div class="icon-ring" style="margin-top:39px">
      <svg width="50" height="40" viewBox="0 0 50 40" fill="#fff"><rect x="16" y="4" width="17" height="13"/><rect x="4" y="20" width="17" height="13"/><rect x="28" y="20" width="17" height="13"/></svg>
    </div>
    <div class="tile-title" style="margin-top:22px">About Us</div>
  </section>

  <section class="block tile services">
    <div class="icon-ring" style="margin-top:47px">
      <svg width="36" height="42" viewBox="0 0 36 42" fill="none" stroke="#fff" stroke-width="3"><path d="M3 2 H24 L33 11 V40 H3 Z"/><path d="M10 20 H26 M10 27 H26 M10 34 H26"/></svg>
    </div>
    <div class="tile-title" style="margin-top:12px">Services Offered</div>
  </section>

  <section class="block tile testimonials">
    <div class="icon-ring" style="margin-top:45px">
      <svg width="50" height="40" viewBox="0 0 50 40" fill="#fff"><rect x="16" y="4" width="17" height="13"/><rect x="4" y="20" width="17" height="13"/><rect x="28" y="20" width="17" height="13"/></svg>
    </div>
    <div class="tile-title" style="margin-top:12px">Testimonials</div>
  </section>

  <section class="block tile newsletter">
    <div class="icon-ring" style="margin-top:46px">
      <svg width="44" height="40" viewBox="0 0 44 40" fill="#fff"><path d="M40 3 L3 20 L15 24 Z"/><path d="M40 3 L18 26 L22 38 Z"/></svg>
    </div>
    <div class="tile-title" style="margin-top:16px">Our Newsletter</div>
  </section>

  <section class="block tile follow">
    <div class="tile-title" style="margin-top:48px">Follow Us</div>
    <div class="row-icons">
      <div class="small-ring" style="background:#fff"></div>
      <div class="small-ring"></div>
      <div class="small-ring"></div>
    </div>
  </section>

  <section class="block tile contact">
    <div class="tile-title" style="margin-top:48px">Contact Us</div>
    <div class="row-icons" style="gap:40px;margin-top:24px">
      <div class="small-ring" style="width:60px;height:60px">
        <svg width="22" height="22" viewBox="0 0 22 22" fill="#fff"><path d="M4 1 L8 1 L10 6 L7 8 Q9 13 14 15 L16 12 L21 14 L21 18 Q20 21 17 21 Q4 19 1 5 Q1 2 4 1 Z"/></svg>
      </div>
      <div class="small-ring" style="width:60px;height:60px">
        <svg width="24" height="24" viewBox="0 0 24 24" fill="#fff"><rect x="1" y="8" width="6" height="15" rx="1"/><path d="M9 2 H19 V8 H23 V23 H9 Z"/><g fill="#d81b0b"><rect x="12" y="11" width="2.5" height="2.5"/><rect x="16" y="11" width="2.5" height="2.5"/><rect x="12" y="15" width="2.5" height="2.5"/><rect x="16" y="15" width="2.5" height="2.5"/><rect x="12" y="19" width="2.5" height="2.5"/><rect x="16" y="19" width="2.5" height="2.5"/></g></svg>
      </div>
      <div class="small-ring" style="width:58px;height:58px">
        <svg width="24" height="18" viewBox="0 0 24 18" fill="none" stroke="#fff" stroke-width="2"><rect x="1" y="1" width="22" height="16" rx="2"/><path d="M1 3 L12 11 L23 3"/></svg>
      </div>
    </div>
  </section>

  <footer class="block footer">All Right Reserved. Copyright ©2015 Company Name</footer>

</div>
</body>
</html>
```